Website template needed for new company in va beach
We plan to flatten anyone who tries competing; Website should be unique
Company name: Pemberfold Cove.... We'll sell quality items cheap. The average customer will think he/she is getting a major steal. With a great location, aggressive advertising and pros ready to work when generous owner needs a break, success is in our future... Products are mostly used and include furniture, antiques, tools, poker supplies, medical supplies, books, home improvement supplies, horticulture equipment, pottery, other art forms.
Likes: drawings, surrealism, satire, comedy, tomas verlunde, otis grembly, fishing, gambling, guns, pottery, web design..... Dislikes: copycats, slobs, liberals, high prices
Masculine
navy
sky blue or aquamarine
left side
http://img207.snapvaultix.net/img207/5813/1zorvelmika.jpg
http://my.framtuckle.com/vault2/KRTLOPNQXZ.jpg
http://img362.snapvaultix.net/img362/71/pfc1.png
#3 website is our logo. . We will sell at the store and online, have specials, offer the cheapest consignment rates anywhere plus always look to improve website content. We may end up advertising pfcove.com because it's easier to remember and type. We might do auctions onsite and online. To give you an idea on our prices, I'm going to offer $1 webhosting per month (unlimited everything). I don't want $2. Customers should feel like they're getting the best deal. They will learn to trust us very quickly .Competition will hate us but if they make it known, we'll stomp them. Good luck.

```html
<!DOCTYPE html>
<html lang="en">
<head>
<meta charset="utf-8">
<title>Pemberfold Cove</title>
<link rel="stylesheet" href="https://fonts.googleapis.com/css2?family=Open+Sans:wght@400;600;700&display=swap">
<style>
  :root {
    --page-bg: #eaf1f7;
    --page-light: #f7fafc;
    --navy: #1f4e86;
    --navy-dark: #173d6b;
    --sky: #5b8fd0;
    --sky-soft: #cfe0f2;
    --silver: #cfd8e1;
    --silver-dark: #a9b6c3;
    --orange: #f39a1e;
    --orange-dark: #d9780c;
    --olive: #8a9a3a;
    --text: #4d6886;
    --text-muted: #6d7f92;
    --white: #ffffff;
  }
  * { box-sizing: border-box; margin: 0; padding: 0; }
  html, body { width: 1200px; height: 1000px; overflow: hidden; }
  body {
    position: relative;
    font-family: "Open Sans", sans-serif;
    background: linear-gradient(180deg, var(--page-light) 0%, var(--page-bg) 100%);
    color: var(--text);
  }
  .decor { position: absolute; inset: 0; }
  .hero-photo {
    position: absolute; left: 0; top: 0; width: 325px; height: 255px;
    background: radial-gradient(ellipse at 40% 45%, #f0a040 0%, #d66a2a 35%, #b9c7d3 75%, #dfe6ec 100%);
    border-bottom-right-radius: 60px;
  }
  .brand { position: absolute; left: 345px; top: 0; display: flex; align-items: flex-start; gap: 14px; }
  .brand-mark {
    width: 136px; height: 136px; border-radius: 50%;
    background: var(--white); border: 4px solid var(--silver-dark);
  }
  .brand-text { padding-top: 34px; }
  .brand-name { font-size: 30px; font-weight: 700; color: var(--orange); letter-spacing: 1px; }
  .brand-tagline { font-size: 17px; color: var(--sky); line-height: 22px; margin-top: 4px; }

  .main-nav a {
    position: absolute; display: block; text-decoration: none;
    color: var(--olive); font-size: 17px; font-weight: 600;
  }
  .nav-icon {
    position: absolute; width: 50px; height: 50px; border-radius: 8px;
    background: linear-gradient(180deg, #ffb44a, var(--orange-dark));
    border: 2px solid var(--white); box-shadow: 0 2px 4px rgba(0,0,0,.2);
  }
  .nav-icon svg { width: 100%; height: 100%; }
  .nav-rule { position: absolute; width: 1px; background: var(--silver-dark); }

  .side-menu { position: absolute; left: 262px; top: 281px; list-style: none; }
  .side-menu li { display: flex; align-items: center; height: 50px; font-size: 20px; color: var(--text-muted); }
  .side-menu .arrow-box {
    width: 32px; height: 32px; margin-right: 14px; border-radius: 3px;
    background: linear-gradient(180deg, #7c8a98, #56636f);
  }
  .side-menu li:nth-child(3) .arrow-box { background: linear-gradient(180deg, #ffb44a, var(--orange-dark)); }
  .side-menu .arrow-box svg { width: 100%; height: 100%; }

  .gallery-tab {
    position: absolute; left: -20px; top: 452px; width: 58px; height: 58px; border-radius: 50%;
    background: linear-gradient(180deg, #9aa8b5, #6c7a87);
  }
  .gallery-label { position: absolute; left: 40px; top: 468px; font-size: 18px; font-weight: 700; color: var(--orange); }
  .gallery-thumb {
    position: absolute; left: 8px; top: 513px; width: 213px; height: 150px;
    border-radius: 30px 80px 30px 80px; border: 6px solid var(--white);
    background: linear-gradient(135deg, #e7ecf1, #a8b4bf 60%, #c8d1d9);
    box-shadow: 0 2px 6px rgba(0,0,0,.2);
  }
  .promo {
    position: absolute; left: 224px; top: 508px; width: 230px; height: 154px;
    background: var(--sky); border-radius: 4px; overflow: hidden;
  }
  .promo-head {
    display: flex; align-items: center; height: 36px; padding-left: 10px;
    background: var(--navy); color: var(--white); font-size: 17px; font-weight: 700;
  }
  .promo-head span.tri {
    width: 0; height: 0; margin-right: 14px;
    border-left: 9px solid var(--white); border-top: 6px solid transparent; border-bottom: 6px solid transparent;
  }
  .promo-body { padding: 12px 12px; color: var(--white); font-size: 16px; }
  .promo-more {
    position: absolute; left: 428px; top: 650px; width: 38px; height: 38px; border-radius: 50%;
    background: var(--orange); border: 3px solid var(--white);
  }

  .news { position: absolute; left: 97px; top: 700px; width: 260px; }
  .news-title { display: flex; align-items: center; gap: 10px; font-size: 19px; font-weight: 700; color: var(--orange); }
  .news-icon { width: 34px; height: 34px; border-radius: 6px; background: linear-gradient(180deg, #a7b3be, #77858f); }
  .news-item { margin-left: 43px; margin-top: 8px; }
  .news-date { font-size: 13px; color: var(--orange); }
  .news-date::before { content: "\2022 "; }
  .news-text { font-size: 15px; line-height: 22px; color: var(--text-muted); }

  .about { position: absolute; left: 508px; top: 314px; width: 640px; }
  .about h2 { font-size: 17px; font-weight: 700; color: var(--olive); margin-bottom: 12px; }
  .about h2::before { content: "\2022 "; color: var(--orange); }
  .about p span { display: block; font-size: 14.5px; line-height: 20.3px; color: var(--text); }
  .signature { position: absolute; right: 58px; top: 864px; text-align: right; font-size: 15px; line-height: 22px; color: var(--text-muted); }

  .footer-rule { position: absolute; left: 54px; top: 912px; width: 310px; height: 2px; background: var(--silver); }
  .footer-copy { position: absolute; left: 54px; top: 922px; font-size: 14px; line-height: 22px; color: var(--silver-dark); }
  .footer-copy a { color: var(--navy); text-decoration: none; }
  .footer-nav { position: absolute; left: 386px; top: 940px; font-size: 15px; color: var(--navy); }
  .footer-nav span.sep { color: var(--silver-dark); margin: 0 10px; }
</style>
</head>
<body>
  <svg class="decor" width="1200" height="1000" viewBox="0 0 1200 1000" aria-hidden="true">
    <path d="M0 250 C120 330 250 300 330 250 L330 340 C240 380 100 380 0 330 Z" fill="#d8e6f3"/>
    <path d="M0 420 C60 360 150 340 240 350 L240 370 C150 365 70 390 0 450 Z" fill="#c3d6ea"/>
    <path d="M300 260 C500 280 800 120 1200 40 L1200 95 C820 160 520 320 300 300 Z" fill="#d9e1e8"/>
    <path d="M300 300 C520 320 820 160 1200 95" fill="none" stroke="#b3c0cc" stroke-width="3"/>
    <path d="M300 260 C500 280 800 120 1200 40" fill="none" stroke="#ffffff" stroke-width="4"/>
    <path d="M320 0 C360 120 330 200 250 260" fill="none" stroke="#9ec3e6" stroke-width="8" opacity=".6"/>
  </svg>

  <div class="hero-photo" role="img" aria-label="Colourful shredded paper spilling out of a cardboard box"></div>

  <header class="brand">
    <div class="brand-mark"></div>
    <div class="brand-text">
      <div class="brand-name">PEMBERFOLD COVE</div>
      <div class="brand-tagline">We plan to flatten anyone<br>who tries competing</div>
    </div>
  </header>

  <nav class="main-nav">
    <div class="nav-icon" style="left:395px;top:180px"><svg viewBox="0 0 50 50"><circle cx="25" cy="16" r="6" fill="#fff"/><path d="M15 40 Q25 20 35 40 Z" fill="#fff"/></svg></div>
    <a href="#" style="left:452px;top:228px">About</a>
    <div class="nav-rule" style="left:452px;top:254px;height:40px"></div>

    <div class="nav-icon" style="left:553px;top:170px"><svg viewBox="0 0 50 50"><rect x="12" y="18" width="26" height="16" rx="5" fill="#fff"/></svg></div>
    <a href="#" style="left:610px;top:216px">Products</a>
    <div class="nav-rule" style="left:610px;top:242px;height:40px"></div>

    <div class="nav-icon" style="left:705px;top:130px"><svg viewBox="0 0 50 50"><path d="M12 17 L22 25 L12 33 Z M25 17 L35 25 L25 33 Z" fill="#fff"/></svg></div>
    <a href="#" style="left:762px;top:184px">Services</a>
    <div class="nav-rule" style="left:762px;top:210px;height:40px"></div>

    <div class="nav-icon" style="left:845px;top:66px"><svg viewBox="0 0 50 50"><path d="M14 30 L24 14 L36 24 L26 38 Z" fill="#fff"/></svg></div>
    <a href="#" style="left:900px;top:148px">Contacts</a>
    <div class="nav-rule" style="left:900px;top:174px;height:40px"></div>
  </nav>

  <ul class="side-menu">
    <li><span class="arrow-box"><svg viewBox="0 0 32 32"><path d="M10 16 H22 M17 10 L23 16 L17 22" stroke="#fff" stroke-width="3" fill="none"/></svg></span>Finance</li>
    <li><span class="arrow-box"><svg viewBox="0 0 32 32"><path d="M10 16 H22 M17 10 L23 16 L17 22" stroke="#fff" stroke-width="3" fill="none"/></svg></span>Marketing</li>
    <li><span class="arrow-box"><svg viewBox="0 0 32 32"><path d="M10 16 H22 M17 10 L23 16 L17 22" stroke="#fff" stroke-width="3" fill="none"/></svg></span>Human Resources</li>
    <li><span class="arrow-box"><svg viewBox="0 0 32 32"><path d="M10 16 H22 M17 10 L23 16 L17 22" stroke="#fff" stroke-width="3" fill="none"/></svg></span>Sales</li>
  </ul>

  <div class="gallery-tab"></div>
  <div class="gallery-label">Gallery</div>
  <div class="gallery-thumb" role="img" aria-label="Gallery photo of a newspaper page"></div>

  <aside class="promo">
    <div class="promo-head"><span class="tri"></span>www.Somewhere.net</div>
    <div class="promo-body">Anything about that thing!</div>
  </aside>
  <div class="promo-more"><svg viewBox="0 0 32 32" width="32" height="32"><path d="M13 10 L19 16 L13 22" stroke="#fff" stroke-width="3" fill="none"/></svg></div>

  <section class="news">
    <div class="news-title"><span class="news-icon"></span>Last News</div>
    <div class="news-item">
      <div class="news-date">25.07.2003</div>
      <div class="news-text">Sed ut perspiciatis, unde omnis iste natus error sit voluptatem...</div>
    </div>
    <div class="news-item">
      <div class="news-date">25.07.2003</div>
      <div class="news-text">Veritatis et quasi architecto beatae vitae dicta sunt, explicabo...</div>
    </div>
  </section>

  <main class="about">
    <h2>About Us</h2>
    <p>
      <span>We plan to flatten anyoneWe plan to flatten anyone who tries competing</span>
      <span>We plan to flatten anyone who tries competing</span>
      <span>We plan to flatten anyone who tries competing</span>
      <span>We plan to flatten anyoneWe plan to flatten anyone who tries competing</span>
      <span>We plan to flatten anyone who tries competing</span>
      <span>We plan to flatten anyone who tries competing</span>
      <span>We plan to flatten anyoneWe plan to flatten anyone who tries competing</span>
      <span>We plan to flatten anyone who tries competing</span>
      <span>We plan to flatten anyone who tries competing</span>
      <span>We plan to flatten anyoneWe plan to flatten anyone who tries competing</span>
      <span>We plan to flatten anyone who tries competing</span>
      <span>We plan to flatten anyone who tries competing</span>
      <span>We plan to flatten anyoneWe plan to flatten anyone who tries competing</span>
      <span>We plan to flatten anyone who tries competing</span>
      <span>We plan to flatten anyone who tries competing</span>
      <span>We plan to flatten anyoneWe plan to flatten anyone who tries competing</span>
      <span>We plan to flatten anyone who tries competing</span>
      <span>We plan to flatten anyone who tries competing</span>
      <span>We plan to flatten anyoneWe plan to flatten anyone who tries competing</span>
      <span>We plan to flatten anyone who tries competing</span>
      <span>We plan to flatten anyone who tries competing</span>
      <span>We plan to flatten anyoneWe plan to flatten anyone who tries competing</span>
      <span>We plan to flatten anyone who tries competing</span>
      <span>We plan to flatten anyone who tries competing</span>
    </p>
  </main>

  <div class="signature">General art-manager : Dorian Kessel<br>dorian@pfcove.com</div>

  <div class="footer-rule"></div>
  <footer>
    <div class="footer-copy">2003 © Copyright Webdesign Company.<br>All rights Reserved. Read <a href="#">Privacy Policy</a>.</div>
    <div class="footer-nav">About us<span class="sep">|</span>Portfolio<span class="sep">|</span>Services<span class="sep">|</span>Contacts</div>
  </footer>
</body>
</html>
```